Varneck Law Business cards and stationary design project

We are looking for a stationary design for business cards (double sided), 8x10, 5x7, and legal and standard envelopes.

We would like the design to match the logo that we have already.
Color palate preferred is Teal, White, grey and any others that will look good for a professional law firm.

We would like this statement: "RELATIONSHIPS. RESPECT. RESULT" to be on the back of the business cards and maybe on the stationary if it looks good.

Please see link to website for more information: www.varneck-law-example.com

Target Market(s)

Potential clients that need Attorney services.

Industry/Entity Type

Law Firm

Contact Information for Business Card

We would like the front and back to be two different colors. Current business cards are teal front, grey back and are a vertical design. We are open to options with colors.

Font styles to use
Serif

Colors
33a6d7
33b8a4
b9b9b9
5c5c5c

Requirements
Must have
• Logo supplied needs to go on the card and stationary.
• Match website color palate, www.varneck-law-example.com
• Be professional and not too wordy.
• Criminal Law, Civil Litigation, Personal Injury, Restraining Orders need to be on the card.
Nice to have
• RELATIONSHIPS. RESPECT. RESULTS. on the back of the card.
Should not have
• Not be too busy/wordy or too flashy.

```html
<!DOCTYPE html>
<html lang="en">
<head>
<meta charset="utf-8">
<title>Varneck Law – Business Cards</title>
<link rel="stylesheet" href="https://fonts.googleapis.com/css2?family=Lora:wght@400;700&display=swap">
<style>
  :root {
    --backdrop: #262626;
    --card-front: #050505;
    --card-back: #3d4042;
    --teal: #1f93a8;
    --teal-bright: #36b3c9;
    --white: #f2f2f2;
    --grey: #8a8a8a;
    --grey-light: #b9b9b9;
  }
  * { box-sizing: border-box; margin: 0; padding: 0; }
  html, body { width: 1200px; height: 900px; overflow: hidden; }
  body {
    background: var(--backdrop);
    position: relative;
    font-family: "Lora", Georgia, serif;
  }
  .card {
    position: absolute;
    width: 620px;
    height: 354px;
    border-radius: 18px;
  }
  /* Back of card */
  .card-back {
    left: 80px; top: 70px;
    background: var(--card-back);
    display: flex; flex-direction: column;
    align-items: center; justify-content: center;
    text-align: center;
  }
  .card-back .firm-name {
    color: var(--teal-bright);
    font-size: 56px;
    font-weight: 400;
    letter-spacing: 2px;
    margin-bottom: 34px;
  }
  .card-back .website {
    color: var(--white);
    font-size: 15px;
    letter-spacing: 4px;
    margin-bottom: 6px;
  }
  .card-back .tagline {
    color: var(--white);
    font-size: 15px;
    letter-spacing: 1px;
  }
  /* Front of card */
  .card-front {
    left: 500px; top: 476px;
    background: var(--card-front);
    display: flex; align-items: center;
  }
  .brand {
    width: 300px;
    display: flex; flex-direction: column;
    justify-content: center; align-items: center;
    text-align: center;
  }
  .brand .firm-name {
    color: var(--teal);
    font-size: 38px;
    font-weight: 400;
    letter-spacing: 1px;
    margin-bottom: 16px;
  }
  .practice-areas {
    color: var(--grey-light);
    font-size: 11px;
    letter-spacing: 1px;
    line-height: 1.6;
    text-transform: uppercase;
  }
  .divider {
    width: 1px; height: 200px;
    background: var(--grey);
  }
  .contact {
    padding-left: 24px;
    color: var(--teal);
    font-size: 13px;
    line-height: 1.35;
  }
  .contact .person {
    font-size: 19px;
    font-weight: 700;
    letter-spacing: 0.5px;
    line-height: 1.1;
  }
  .contact .role {
    color: var(--white);
    font-size: 13px;
    margin-bottom: 12px;
  }
  .contact .address { margin-bottom: 4px; }
  .contact .line { display: flex; align-items: center; gap: 8px; }
  .contact svg { width: 11px; height: 11px; flex: none; }
</style>
</head>
<body>
  <section class="card card-back">
    <div class="firm-name">Varneck Law</div>
    <div class="website">www.varneck-law-example.com</div>
    <div class="tagline">RELATIONSHIPS. RESPECT. RESULT</div>
  </section>

  <section class="card card-front">
    <div class="brand">
      <div class="firm-name">Varneck Law</div>
      <div class="practice-areas">Criminal Law · Civil Litigation<br>Personal Injury · Restraining Orders</div>
    </div>
    <div class="divider"></div>
    <div class="contact">
      <div class="person">CLAIRE VARNECK</div>
      <div class="role">Lawyer</div>
      <div class="address">4815 Harbor View Ave.<br>#210 Coral Point, CA 90000</div>
      <div class="line">
        <svg viewBox="0 0 12 12" aria-hidden="true"><path d="M2.5 1 L4.5 1 L5.3 3.4 L4 4.4 Q5 6.8 7.6 8 L8.6 6.7 L11 7.5 L11 9.5 Q10.5 11 9 11 Q1 10 1 2.5 Q1 1 2.5 1 Z" fill="#f2f2f2"/></svg>
        <span>(555) 014-2738</span>
      </div>
      <div class="line">
        <svg viewBox="0 0 12 12" aria-hidden="true"><rect x="1" y="2.5" width="10" height="7" fill="none" stroke="#f2f2f2" stroke-width="1.2"/><path d="M1 2.5 L6 6.5 L11 2.5" fill="none" stroke="#f2f2f2" stroke-width="1.2"/></svg>
        <span>claire@varneck-law-example.com</span>
      </div>
      <div class="line">
        <svg viewBox="0 0 12 12" aria-hidden="true"><circle cx="6" cy="6" r="5" fill="none" stroke="#f2f2f2" stroke-width="1.1"/><ellipse cx="6" cy="6" rx="2.2" ry="5" fill="none" stroke="#f2f2f2" stroke-width="1"/><path d="M1 6 H11" stroke="#f2f2f2" stroke-width="1"/></svg>
        <span>www.varneck-law-example.com</span>
      </div>
    </div>
  </section>
</body>
</html>
```